We need to design for New company Based in Oman we are
we need to design

-BANNER
-Flyer
-Pricing List
-Schulde
and other marketing staff

WE need it arabic And English

Falcon Ridge Combat Arts Gym
Oman's Top MMA & Combat Sports Gym
Home of (RVKORE Oman)

Affiliated with one of the world's top Brazilian Jiujitsu Academies (Tidewater Clinch Club)

Train with our team of Professional world class instructors

Be the champion you Are!!!!

-Boxing / Kickboxing
-Muay Thai
-MMA
-Jiujitsu
-Sambo
-Grappling
-Karate
-Taekwondo
-Fitness and conditioning

Overview

Falcon Ridge MMA-
An ultimate destination for all the martial arts and fitness enthusiasts looking to train in Mma, Striking, Grappling or Fitness. Providing them with the best programmes under well accomplished Atheletes and trainers fromm around the world helping them reach their goals and bringing the best out of oneself.

Members of Falcon Ridge MMA
-Suitable for anyone and everyone regardless of the age, weight or gender.
-Anyone interested in becoming a professional Athelete whether in mainstream martial arts or any other similar sports, looking to increase level of strength agility, speed, reflex and cardiovascular endurance.
- Kids above age 5 to gain confidence and fitness.
- Anyone looking to learn real self defense.

Mission statement-
Improving fighter quality and development by increasing the training level to bring out the max. potential.
We also aim to improve the health and fitness in the society through our specialised programmes to have a better life.

Activities done at Falcon Ridge MMA
MMA- A full contact sport that allows includes Striking and grappling techniques both standing and on the ground.
- It is derived from a variety of other combat sports and Martial arts.
-It is the fastest growing sport in the world.

Muay Thai- Combat sport originated from Thailand which is a form of stand up fighting.
- It is known as "The art of Eight Limbs" which is the combined use of fists, eldows, knees and feet.
-A practitioner of Muay Thai thus has the ability to execute strikes using eight "points of contact", as opposed to "two points" ( fists ) in western boxing & "four points" ( fists & feet ) used in the primarily sport oriented forms of Martial arts.

Boxing - It is a sport in which two competitors try to hit each with their gloved encased fists while try to avoid each others blow. Also know as the Manly art of Self Defense.
- one of the most famous sport around the world which involves 10 to 12 rounds of 3 min each in Professional Bouts and 3 Rounds in Amateur bouts .
- a sport not only loved by competitors but also non competitors, as it is very useful in maintaining physical health and fitness.

BJJ- A grappling based martial arts whose central theme is the skill of controlling a resisting opponent in ways that forces him to submit.
- Involving techniques yo overcome greater size, strength and aggression with lesser size and strength is the key not of the sport. It is achieved by utilising superior leverage, grip & position upon your opponent.
-A student of the sport hain a deep understanding of the workings and the limits of the human body.

Wrestling- It is a hand to hand sport involving takedowns, throws, holds, tilts, pinning combination. A scoring system based on control of your opponent.
It is the oldest sport in the recorded history.
07/08/2017, 11:18:03 am: Coach Karim Suleiman: Strength and Conditioning-
Special programs designed to improve co-ordination of body and mind, muscle functioning and weight loss.
A great way to have a healthier, happier and stress free life.
- Intense but fun programmes for all genders and age groups

Target market :
New business Development
9-35 Age
Fresh High school Graduates
Organization , Word of mouth
Referral

Military organization
Oil and gas (LNG , QTV , Zeno , ,,, etc )
School and college

Design preferences
We need the design contain 2 color black and red and the same color

and enter 2 logo in FALCON RIDGE MMA and RVKOman

Arabic Version

الصقر للفنون القتالية
‎مشروع عماني بإدارة اختصاصين في الفنون القتاليه بالتعاون مع اكاديمية (RVKore)البرازيلية للجوجيستو متخصصين في تدريب وتعليم الألعاب والمهارات القتالية
‎- تعليم الفنون الدفاع عن النفس
‎- لعبة الجوجستو البرازيلية
‎- لعبة الموي تاي و الكيك بوكسنج
‎- لعبة السامبو الروسية
‎- الملاكمة
‎-فنون القتال المختلطة MMA
‎-الكارتيه
‎-التايكوندو
تابعونا في الأنستجرام

‏https://instagram.example/p/QTRVx7mLkP2/

موقعنا

Falcon Ridge MMA Gym
Seeb
https://maps.example.net/aKpwRtzLmQe

Target Market(s)

9-35 Age
Referral
Military organization
School and college

Industry/Entity Type

Martial Art

Font styles to use
Sans Serif

Colors
ec1f27
ffffff
000000

Requirements
Must have
• 2 logo in the Falcon Ridge MMA
• and Rvk Oman
• Brand Mark : Logo ( Falcon Ridge MMA ) with name Falcon Ridge Combat Arts
Nice to have
• it's Mix Martial Arts Gym With

```html
<!DOCTYPE html>
<html lang="ar">
<head>
<meta charset="utf-8">
<title>Falcon Ridge MMA Flyer</title>
<link href="https://fonts.googleapis.com/css2?family=Cairo:wght@400;600;800&family=Saira+Condensed:wght@500;600&display=swap" rel="stylesheet">
<style>
  :root {
    --brand-red: #ec1f27;
    --ink: #000000;
    --paper: #ffffff;
    --headline-grey: #d9d9d9;
    --body-grey: #ececec;
    --bullet-grey: #d4d4d4;
  }
  * { box-sizing: border-box; margin: 0; padding: 0; }
  html, body { width: 1200px; height: 1200px; overflow: hidden; background: var(--paper); }
  .flyer {
    position: absolute; left: 168px; top: 42px; width: 862px; height: 1115px;
    background: var(--ink); overflow: hidden; font-family: "Cairo", sans-serif;
    box-shadow: -14px 12px 0 #4a4a4a;
  }
  .flyer__photo {
    position: absolute; inset: 0;
    background:
      radial-gradient(ellipse 120px 150px at 330px 150px, #a0705a 0%, #7a4c36 45%, rgba(60,36,26,0) 100%),
      radial-gradient(ellipse 260px 300px at 230px 420px, #a3674a 0%, #7d4a33 45%, rgba(70,40,28,.55) 75%, rgba(0,0,0,0) 100%),
      radial-gradient(ellipse 90px 70px at 420px 410px, #d8d4d0 0%, #9d9894 50%, rgba(120,110,100,0) 100%),
      radial-gradient(ellipse 220px 150px at 560px 640px, #93603f 0%, #6e432e 50%, rgba(60,36,26,0) 100%),
      radial-gradient(ellipse 300px 220px at 260px 760px, #242220 0%, #161514 60%, rgba(20,20,20,0) 100%),
      radial-gradient(ellipse 170px 230px at 470px 960px, #8a5a40 0%, #5c3a2a 55%, rgba(40,26,20,0) 100%),
      radial-gradient(ellipse 330px 260px at 620px 830px, rgba(200,200,200,.35) 0%, rgba(120,120,120,.15) 55%, rgba(0,0,0,0) 100%),
      linear-gradient(160deg, #151312 0%, #0a0a0a 60%, #111 100%);
  }
  .logo { position: absolute; display: flex; align-items: center; justify-content: center; gap: 8px;
    color: var(--paper); font-weight: 800; text-align: center; line-height: 1.05; }
  .logo--partner { left: 478px; top: 70px; width: 176px; height: 112px; font-size: 21px; }
  .logo--partner .logo__mark { width: 24px; height: 24px; border-radius: 50%; background: var(--brand-red); flex: none; }
  .logo--club { left: 656px; top: 54px; width: 162px; height: 142px; font-size: 22px; }
  .headline { position: absolute; right: 60px; top: 218px; width: 400px; text-align: center;
    color: var(--headline-grey); font-weight: 800; direction: rtl; text-shadow: 0 2px 4px #000; }
  .headline__line { display: block; font-size: 50px; line-height: 62px; }
  .intro { position: absolute; right: 48px; top: 350px; width: 460px; direction: rtl;
    color: var(--body-grey); font-size: 26px; line-height: 35px; text-align: right; text-shadow: 0 1px 3px #000; }
  .intro__accent { color: var(--brand-red); font-family: "Saira Condensed", sans-serif; font-weight: 500; }
  .programmes { position: absolute; right: 54px; top: 0; width: 320px; height: 100%; list-style: none; direction: rtl; }
  .programmes__item { position: absolute; right: 0; padding-right: 40px; color: var(--body-grey);
    font-size: 23px; line-height: 28px; text-shadow: 0 1px 3px #000; white-space: nowrap; }
  .programmes__item::before { content: ""; position: absolute; right: 0; top: 0;
    width: 30px; height: 30px; border-radius: 50%; background: var(--bullet-grey); }
  .contact { position: absolute; left: 48px; top: 955px; font-family: "Saira Condensed", sans-serif;
    font-weight: 600; color: var(--paper); font-size: 33px; }
  .contact__row { display: flex; align-items: center; gap: 14px; height: 54px; }
  .contact__dot { width: 44px; height: 44px; border: 4px solid var(--brand-red); border-radius: 50%; }
  .address { position: absolute; left: 498px; top: 979px; width: 331px; height: 75px; background: var(--ink);
    color: var(--paper); font-family: "Saira Condensed", sans-serif; font-weight: 500; font-size: 16px;
    line-height: 20px; padding: 8px 6px 0 28px; }
  .address svg { position: absolute; left: 10px; top: 12px; }
</style>
</head>
<body>
  <main class="flyer">
    <div class="flyer__photo" role="img" aria-label="Photo of a shirtless fighter in MMA gloves and dark shorts throwing a knee strike through splashing water on a black background"></div>

    <div class="logo logo--partner"><span class="logo__mark"></span><span>RVKORE<br>Oman</span></div>
    <div class="logo logo--club">FALCON RIDGE<br>MMA</div>

    <h1 class="headline">
      <span class="headline__line">الصقر</span>
      <span class="headline__line">للفنون القتالية</span>
    </h1>

    <p class="intro">مشروع عماني بإدارة اختصاصين<br>في الفنون القتاليه بالتعاون<br>مع اكاديمية (<span class="intro__accent">RVKORE</span>)البرازيلية<br>للجوجيستو</p>

    <ul class="programmes">
      <li class="programmes__item" style="top:528px">تعليم الفنون الدفاع<br>عن النفس</li>
      <li class="programmes__item" style="top:590px">لعبة السامبو<br>الروسية</li>
      <li class="programmes__item" style="top:652px">فنون القتال المختلطة<br>MMA</li>
      <li class="programmes__item" style="top:713px">التايكوندو</li>
      <li class="programmes__item" style="top:762px">لعبة الجوجستو<br>البرازيلية</li>
      <li class="programmes__item" style="top:822px">لعبة الموي تاي<br>و الكيك بوكسنج</li>
      <li class="programmes__item" style="top:892px">الملاكمة</li>
      <li class="programmes__item" style="top:940px">الكارتيه</li>
    </ul>

    <div class="contact">
      <div class="contact__row"><span class="contact__dot"></span><span>FALCONRIDGE.MMA</span></div>
      <div class="contact__row">
        <svg width="56" height="32" viewBox="0 0 56 32" aria-hidden="true">
          <rect x="2" y="2" width="52" height="28" rx="5" fill="none" stroke="#ec1f27" stroke-width="4"/>
          <rect x="6" y="6" width="5" height="20" fill="#ec1f27"/>
        </svg>
        <span>+973 9000 4812</span>
      </div>
    </div>

    <div class="address">
      <svg width="12" height="17" viewBox="0 0 12 17" aria-hidden="true">
        <path d="M6 0a6 6 0 0 0-6 6c0 4.5 6 11 6 11s6-6.5 6-11a6 6 0 0 0-6-6zm0 8.5a2.5 2.5 0 1 1 0-5 2.5 2.5 0 0 1 0 5z" fill="#ffffff"/>
      </svg>
      Palm Crescent Street, Seeb Block 12<br>Building of the Noor Al Maarifa Bookshop<br>Second Floor
    </div>
  </main>
</body>
</html>
```